Home page web design for "Tales from Thee"

We need a home page web design for a start up company that will write memoirs for seniors.
The completed project will need to include PSD files...NO HTML or CSS necessary.
Attached is a brief outline concept that may give you some ideas...but you are the creative professionals, so please feel free to add your ideas. We will also attach some files that show you our logo, brochures, and photos that could be used to give you ideas of our focus.
There will need to be access to the other pages on the home page to include: 'About Us'; 'How We Can Help'; 'Community Sessions'; 'Senior Consulting ' and 'Contact Us'.
Updates

Target Market(s)

Seniors and Baby Boomers

Industry/Entity Type

It Company

Number of Pages Required

1 page

Colors
f9ba93
fbca95
faa54b
faf289
f37123

Requirements
Must have
• Script easy on senior eyes.
• Initial contact number would be 844-4LANTERN
Nice to have
• While the color pallet is non-specific we prefer the warm colors.
• salmon, peach.......
• NOT so much the orange of Halloween:)
• However, please utilize your creativity and put in colors you feel will draw best with your design.

```html
<!DOCTYPE html>
<html lang="en">
<head>
<meta charset="utf-8">
<title>Tales from Thee — Home</title>
<link rel="stylesheet" href="https://fonts.googleapis.com/css2?family=Roboto+Condensed:wght@500;700&family=Ubuntu:wght@400&family=Dancing+Script:wght@700&display=swap">
<style>
  :root {
    --orange: #f37123;
    --orange-soft: #f9ba93;
    --peach: #fbca95;
    --ink: #1f1f1f;
    --paper: #f6f4f1;
    --white: #ffffff;
  }
  * { box-sizing: border-box; margin: 0; padding: 0; }
  html, body { width: 965px; height: 1200px; overflow: hidden; }
  body { position: relative; background: var(--paper); font-family: "Ubuntu", sans-serif; color: var(--ink); }

  .site-header { position: absolute; top: 0; left: 0; width: 965px; height: 92px; background: var(--white); z-index: 3; }
  .brand-badge {
    position: absolute; left: 58px; top: -10px; width: 302px; height: 165px;
    background: var(--white); border-radius: 50%;
    display: flex; align-items: center; justify-content: center; z-index: 4;
  }
  .brand-name { font-family: "Ubuntu", sans-serif; font-size: 27px; color: var(--orange); margin-top: -12px; }

  .main-nav { position: absolute; top: 29px; left: 350px; display: flex; align-items: center; }
  .main-nav a {
    font-family: "Roboto Condensed", sans-serif; font-weight: 500; font-size: 14px;
    color: var(--ink); text-decoration: none; height: 30px; line-height: 30px; margin-right: 17px;
  }
  .main-nav a.is-active { background: var(--orange); color: var(--white); padding: 0 14px; border-radius: 2px; margin-right: 13px; }
  .main-nav a:nth-child(2) { margin-right: 25px; }

  .hero { position: absolute; top: 92px; left: 0; width: 965px; height: 420px; }
  .hero-photo { position: absolute; inset: 0; background: linear-gradient(100deg, #5e3218 0%, #9b5a30 30%, #b87448 55%, #c98c63 75%, #d9b193 100%); }
  .hero-arrow { position: absolute; top: 175px; }
  .hero-arrow.prev { left: 77px; }
  .hero-arrow.next { left: 860px; }
  .hero-caption {
    position: absolute; left: 80px; top: 358px;
    font-family: "Dancing Script", cursive; font-size: 36px; color: var(--white);
  }

  .intro { position: absolute; top: 512px; left: 0; width: 965px; height: 605px; }
  .intro-backdrop { position: absolute; inset: 0; background: linear-gradient(180deg, #f7f5f2 0%, #ece6e0 50%, #e4dcd5 100%); }
  .intro-title {
    position: absolute; top: 24px; left: 0; width: 965px; text-align: center;
    font-family: "Dancing Script", cursive; font-size: 29px; color: var(--ink);
  }
  .intro-flourish { position: absolute; top: 66px; left: 431px; width: 103px; height: 16px; background: var(--orange-soft); border-radius: 8px; }
  .intro-copy { position: absolute; top: 102px; left: 99px; width: 770px; font-size: 15.6px; line-height: 20px; }
  .intro-copy p { margin-bottom: 20px; }
  .intro-copy .lead { color: var(--orange); }

  .gift-art { position: absolute; left: 90px; top: 497px; width: 88px; height: 84px; background: linear-gradient(160deg, #f6c84a, #d89a1c); border-radius: 4px; }
  .gift-label { position: absolute; left: 188px; top: 518px; font-family: "Dancing Script", cursive; font-size: 28px; color: var(--ink); }

  .learn-more {
    position: absolute; left: 587px; top: 497px; width: 204px; height: 65px;
    background: var(--orange); border-radius: 3px; display: flex; align-items: center;
    padding-left: 17px; text-decoration: none;
  }
  .learn-more span { font-family: "Dancing Script", cursive; font-size: 27px; color: var(--white); margin-left: 12px; }

  .site-footer { position: absolute; top: 1117px; left: 0; width: 965px; height: 83px; background: var(--orange); text-align: center; font-family: Arial, sans-serif; font-weight: 700; }
  .footer-contact { margin-top: 19px; font-size: 13.8px; color: var(--white); }
  .footer-contact b { color: #111; }
  .footer-legal { margin-top: 15px; font-size: 10px; font-weight: 400; color: #111; }
  .footer-legal strong { color: var(--white); }
</style>
</head>
<body>
  <header class="site-header">
    <div class="brand-badge"><span class="brand-name">Tales from Thee</span></div>
    <nav class="main-nav">
      <a href="#" class="is-active">About Us</a>
      <a href="#">How We Can Help</a>
      <a href="#">Community Sessions</a>
      <a href="#">Senior Consulting Services</a>
      <a href="#">Contact</a>
    </nav>
  </header>

  <section class="hero">
    <div class="hero-photo" role="img" aria-label="Warm sepia photo of an elderly woman reading old letters beside an oil lamp and bookshelf"></div>
    <svg class="hero-arrow prev" width="24" height="58" viewBox="0 0 24 58"><polyline points="20,2 3,29 20,56" fill="none" stroke="#fff" stroke-width="2"/></svg>
    <svg class="hero-arrow next" width="24" height="58" viewBox="0 0 24 58"><polyline points="4,2 21,29 4,56" fill="none" stroke="#fff" stroke-width="2"/></svg>
    <p class="hero-caption">Ordinary Lives.....Extraordinary Legacies</p>
  </section>

  <main class="intro">
    <div class="intro-backdrop" role="img" aria-label="Faded photo of an elderly couple walking along a beach with family"></div>
    <h1 class="intro-title">When a genealogy doesn't say enough!</h1>
    <div class="intro-flourish" role="img" aria-label="Decorative flourish"></div>
    <div class="intro-copy">
      <p class="lead">If you were alive in 100 years, what would you share with your descendants?</p>
      <p class="lead">Now you have a vehicle to help you immortalize your thoughts for the future...specifically for those who will want to know!</p>
      <p>We are not all presidents of countries or CEO’s of fortune 500 companies! But “every life legacy is a gift to be treasured by the next generation.”</p>
      <p>Does your family host generations of soldiers, doctors, farmers, scientists, mechanics, entrepreneurs, writers, politicians, contractors, pastors, artisans, athletes, musicians, etc..? Generational patterns can often emerge when writing your story that will interest the next generation.</p>
      <p>A genealogy, while very relevant, doesn’t offer the personal story of the names we find. A biography can place a deeper relevance on the face for future descendants. Every life is a legacy to pass forward and we at Tales from Thee believe everyone should chronicle their life journey in writing. This commitment allows you to be remembered for who you truly are as a person.</p>
      <p>Think about it....Do you know the triumphs and tribulations of your ancestors? Do you wish you did? Well, so will those falling into your personal family tree.</p>
    </div>
    <div class="gift-art" role="img" aria-label="Golden wrapped gift box with red ribbon"></div>
    <p class="gift-label">Great Gift Ideas</p>
    <a href="#" class="learn-more">
      <svg width="44" height="42" viewBox="0 0 44 42"><path d="M10 4h26a3 3 0 0 1 3 3l-4 28a3 3 0 0 1-3 3H8a4 4 0 0 1-4-4l3-27a3 3 0 0 1 3-3z" fill="none" stroke="#fff" stroke-width="3.5" stroke-linejoin="round"/><line x1="15" y1="12" x2="31" y2="12" stroke="#fff" stroke-width="3"/><line x1="14" y1="19" x2="30" y2="19" stroke="#fff" stroke-width="3"/></svg>
      <span>Learn More</span>
    </a>
  </main>

  <footer class="site-footer">
    <p class="footer-contact"><b>Our Address :</b> Office No., Area Name, City State Country. &nbsp;<b>Call :</b> &nbsp;844-4LANTERN &nbsp;<b>Email :</b> &nbsp;hello@talesfromthee.com</p>
    <p class="footer-legal">© <strong>Tales from Thee</strong> - 2014. All Rights Reserved.</p>
  </footer>
</body>
</html>
```